Business Card - Ridge Wellness

Please use the logo / design elements and font to design a business card that is eye catching and informative. If using "Direct Primary Care" logo element, you don't have to spell it out in the text.

Dr. Calvin Pettrow
Ridge Wellness - Direct Primary Care
4817 Tallow Creek Rd. Suite 305
Alder Bend, QX 40871
Phone: 555-555-0173
RidgeWellnessQX.com

```html
<!DOCTYPE html>
<html lang="en">
<head>
<meta charset="utf-8">
<title>Ridge Wellness Business Card</title>
<link href="https://fonts.googleapis.com/css2?family=Poppins:wght@500;700&family=Arimo:wght@400&display=swap" rel="stylesheet">
<style>
  :root {
    --backdrop: #e4e4e4;
    --card-white: #ffffff;
    --navy: #0b1538;
    --navy-deep: #021133;
    --navy-emboss: #0c2466;
    --accent-blue: #1f5fd6;
    --text-grey: #454545;
    --divider: #b9b9b9;
  }
  * { margin: 0; padding: 0; box-sizing: border-box; }
  html, body { width: 1200px; height: 1200px; overflow: hidden; }
  body { background: var(--backdrop); position: relative; font-family: 'Arimo', Arial, sans-serif; }

  .card { position: absolute; width: 689px; height: 394px; overflow: hidden; }
  .card-front { left: 267px; top: 159px; background: var(--card-white); }
  .card-back { left: 262px; top: 653px; background: var(--navy-deep); }

  .brand {
    position: absolute; display: flex; align-items: center; gap: 10px;
    font-family: 'Poppins', sans-serif; font-weight: 500; white-space: nowrap;
  }
  .brand-front { left: 205px; top: 212px; transform: translate(-50%, -50%); font-size: 33px; color: var(--navy); }
  .brand-dot { width: 16px; height: 16px; border-radius: 50%; background: var(--accent-blue); flex: none; }

  .divider { position: absolute; left: 356px; top: 116px; width: 2px; height: 158px; background: var(--divider); }

  .details { position: absolute; left: 380px; top: 112px; }
  .doctor-name { font-family: 'Poppins', sans-serif; font-weight: 700; font-size: 26px; color: var(--navy); line-height: 1.2; margin-bottom: 14px; }
  .address { font-size: 16px; color: var(--text-grey); line-height: 20px; margin-bottom: 9px; }
  .contact-list { list-style: none; }
  .contact-item { display: flex; align-items: center; font-size: 16px; color: var(--text-grey); line-height: 20.5px; }
  .contact-item svg { width: 14px; height: 14px; margin-right: 12px; flex: none; }

  .stripe-thin { position: absolute; left: 0; right: 0; top: 372px; height: 3px; background: var(--accent-blue); }
  .stripe-band { position: absolute; left: 0; right: 0; top: 377px; height: 17px; background: var(--navy-deep); }

  .brand-back { left: 344px; top: 232px; transform: translate(-50%, -50%); font-size: 56px; color: var(--navy-emboss); }
  .brand-back .brand-dot { width: 24px; height: 24px; background: var(--navy-emboss); }
</style>
</head>
<body>
  <section class="card card-front">
    <div class="brand brand-front"><span class="brand-dot"></span>Ridge Wellness</div>
    <div class="divider"></div>
    <div class="details">
      <h1 class="doctor-name">Dr. Calvin Pettrow</h1>
      <p class="address">4817 Tallow Creek Rd. Suite 305<br>Alder Bend, QX 40871</p>
      <ul class="contact-list">
        <li class="contact-item">
          <svg viewBox="0 0 24 24"><path fill="#1f5fd6" d="M6.6 10.8a15.1 15.1 0 0 0 6.6 6.6l2.2-2.2a1 1 0 0 1 1-.25 11.4 11.4 0 0 0 3.6.57 1 1 0 0 1 1 1V20a1 1 0 0 1-1 1A17 17 0 0 1 3 4a1 1 0 0 1 1-1h3.5a1 1 0 0 1 1 1c0 1.25.2 2.45.57 3.57a1 1 0 0 1-.25 1z"/></svg>
          555-555-0173
        </li>
        <li class="contact-item">
          <svg viewBox="0 0 24 24"><rect x="2" y="5" width="20" height="14" fill="#1f5fd6"/><path d="M2 5l10 8 10-8" fill="none" stroke="#fff" stroke-width="2"/></svg>
          info@ridgewellnessqx.com
        </li>
        <li class="contact-item">
          <svg viewBox="0 0 24 24"><circle cx="12" cy="12" r="10" fill="#1f5fd6"/><path d="M2 12h20M12 2c3 3 3 17 0 20M12 2c-3 3-3 17 0 20" fill="none" stroke="#fff" stroke-width="1.5"/></svg>
          www.RidgeWellnessQX.com
        </li>
      </ul>
    </div>
    <div class="stripe-thin"></div>
    <div class="stripe-band"></div>
  </section>

  <section class="card card-back">
    <div class="brand brand-back"><span class="brand-dot"></span>Ridge Wellness</div>
  </section>
</body>
</html>
```